Cradle Glow Events

New Company ,I will attened clients personal residents(venu of there choice) and provide 3D ultra sound photos at time of ultra sound.This is a Non diagnostic ultra sound which does not replace the ultrasound reqested by Dr.The best time for ultra sound is 24 to 34 weeks.The baby sex can be kept confidential if requied and all cultral and diverse backgrounds cattered for..No referal requied for this.I have 2 main packges,1 baby shower and 2 family time.Extra options available are entertainment,Family time prior to baby shower for dad,decoration, Kids entertainment.
Contact number is 0471938402 email to be added ASAP.
prices start from $450

It Company

```html
<!DOCTYPE html>
<html lang="en">
<head>
<meta charset="utf-8">
<title>Cradle Glow Events – 3D Ultrasound Flyer</title>
<link rel="stylesheet" href="https://fonts.googleapis.com/css2?family=Lily+Script+One&family=Open+Sans:ital,wght@0,400;0,600;1,400&display=swap">
<style>
  :root {
    --magenta: #d41f5f;
    --magenta-deep: #c2134f;
    --orange: #f7941d;
    --white: #ffffff;
    --page: #efeae4;
    --photo-light: #f3ece8;
    --photo-mid: #d9c7bd;
    --photo-warm: #b9896a;
    --shoes-tone: #9aa0b4;
    --shoes-light: #e4e6ec;
  }
  * { margin: 0; padding: 0; box-sizing: border-box; }
  html, body { width: 1200px; height: 899px; overflow: hidden; background: var(--page); }

  .flyer {
    position: absolute; left: 318px; top: 29px;
    width: 576px; height: 826px;
    background: var(--white);
    overflow: hidden;
    box-shadow: 0 2px 10px rgba(0,0,0,.12);
    font-family: 'Lily Script One', cursive;
  }
  .flyer-backdrop { position: absolute; inset: 0; }

  .brand {
    position: absolute; left: 45px; top: 42px;
    display: flex; align-items: center; gap: 10px;
    font-family: 'Open Sans', sans-serif; font-weight: 600;
    font-size: 25px; line-height: 1.05; color: var(--magenta);
    width: 220px;
  }
  .brand-dot { width: 16px; height: 16px; border-radius: 50%; background: var(--orange); flex: none; }

  .contact { position: absolute; left: 297px; top: 46px; color: var(--magenta); }
  .contact-row { display: flex; align-items: center; gap: 10px; white-space: nowrap; line-height: 1; }
  .contact-phone { font-size: 27px; letter-spacing: 1px; }
  .contact-email { font-size: 20px; margin-top: 10px; }
  .contact-row svg { flex: none; }

  .photo-model {
    position: absolute; left: 8px; top: 151px; width: 252px; height: 675px;
    border-radius: 120px 120px 0 0;
    background: linear-gradient(180deg, var(--photo-warm) 0%, var(--photo-mid) 18%, var(--photo-light) 45%, #e6e2df 100%);
  }

  .headline { position: absolute; left: 272px; width: 266px; text-align: center; }
  .headline-3d {
    top: 180px; font-family: 'Open Sans', sans-serif; font-weight: 400;
    font-size: 60px; line-height: 1; color: var(--orange);
  }
  .headline-service { top: 250px; font-size: 24px; line-height: 29px; color: var(--white); font-weight: 400; }
  .headline-options {
    top: 327px; font-family: 'Open Sans', sans-serif; font-weight: 400;
    font-size: 29px; line-height: 36px; color: var(--orange);
  }

  .package-list { position: absolute; left: 317px; top: 385px; list-style: none; color: var(--white); }
  .package-list li {
    position: relative; padding-left: 24px; font-size: 20px; line-height: 26px;
  }
  .package-list li::before {
    content: ""; position: absolute; left: 0; top: 7px;
    width: 14px; height: 14px; border-radius: 50%; background: var(--orange);
  }
  .package-list li.confidential { margin-top: 2px; }
  .package-list li.extra { margin-top: 6px; }

  .extras {
    position: absolute; left: 343px; top: 537px; width: 185px;
    font-family: 'Open Sans', sans-serif; font-style: italic;
    font-size: 13px; line-height: 21px; color: var(--orange);
  }

  .photo-shoes {
    position: absolute; left: 312px; top: 655px; width: 142px; height: 80px;
    border-radius: 10px;
    background: radial-gradient(ellipse at 50% 45%, var(--shoes-tone) 0%, var(--shoes-light) 75%, rgba(228,230,236,0.7) 100%);
  }

  .price-badge {
    position: absolute; left: 474px; top: 660px; width: 72px; height: 72px;
    border-radius: 50%; background: var(--orange);
    outline: 2px dashed var(--white); outline-offset: -5px;
    display: flex; flex-direction: column; align-items: center; justify-content: center;
    font-family: 'Open Sans', sans-serif; color: var(--white); line-height: 1;
  }
  .price-from { font-size: 13px; font-style: italic; margin-bottom: 3px; }
  .price-amount { font-size: 19px; font-weight: 600; }

  .signoff {
    position: absolute; left: 270px; width: 290px; top: 768px;
    text-align: center; font-size: 23px; line-height: 30px; color: var(--magenta);
  }
</style>
</head>
<body>
  <main class="flyer">
    <svg class="flyer-backdrop" width="576" height="826" viewBox="0 0 576 826" aria-hidden="true">
      <defs>
        <linearGradient id="bandFill" x1="0" y1="0" x2="0" y2="1">
          <stop offset="0" stop-color="var(--magenta)"/>
          <stop offset="1" stop-color="var(--magenta-deep)"/>
        </linearGradient>
      </defs>
      <path d="M0 186 C 200 176, 400 140, 576 122 L 576 712 C 420 748, 220 790, 0 805 Z" fill="url(#bandFill)"/>
      <g fill="#ffffff" opacity="0.1">
        <circle cx="40" cy="300" r="50"/>
        <circle cx="250" cy="365" r="70"/>
        <circle cx="470" cy="245" r="80"/>
        <circle cx="540" cy="175" r="60"/>
        <circle cx="545" cy="600" r="55"/>
        <circle cx="320" cy="655" r="45"/>
      </g>
    </svg>

    <div class="brand">
      <span class="brand-dot"></span>
      <span class="brand-name">Cradle Glow<br>Events</span>
    </div>

    <div class="contact">
      <div class="contact-row contact-phone">
        <svg width="16" height="26" viewBox="0 0 16 26" aria-hidden="true">
          <rect x="1.5" y="4" width="13" height="20.5" rx="3" fill="none" stroke="var(--magenta)" stroke-width="2.5"/>
          <rect x="4.5" y="7.5" width="7" height="6" fill="var(--magenta)"/>
          <line x1="4" y1="0.5" x2="4" y2="5" stroke="var(--magenta)" stroke-width="2.5"/>
        </svg>
        <span>0471938402</span>
      </div>
      <div class="contact-row contact-email">
        <svg width="26" height="17" viewBox="0 0 28 18" aria-hidden="true">
          <rect x="1.5" y="1.5" width="25" height="15" fill="none" stroke="var(--magenta)" stroke-width="2.5"/>
          <path d="M1.5 1.5 L14 10 L26.5 1.5" fill="none" stroke="var(--magenta)" stroke-width="2.5"/>
        </svg>
        <span>hi@cradleglow.com</span>
      </div>
    </div>

    <div class="photo-model" role="img" aria-label="Photo of a pregnant woman in white clothes, holding her belly and looking down"></div>

    <h1 class="headline headline-3d">3D</h1>
    <p class="headline headline-service">ultra sound photos<br>at your home!</p>
    <h2 class="headline headline-options">Custom options</h2>

    <ul class="package-list">
      <li>Baby Shower</li>
      <li>Family Time</li>
      <li class="confidential">The baby sex can be<br>kept confidential</li>
      <li class="extra">Extra options:</li>
    </ul>

    <p class="extras">entertainment, baby shower for dad, kids entertainment, decoration,</p>

    <div class="photo-shoes" role="img" aria-label="Photo of a pair of baby sneakers"></div>

    <div class="price-badge">
      <span class="price-from">from</span>
      <span class="price-amount">$450</span>
    </div>

    <p class="signoff">Can’t wait to see you!</p>
  </main>
</body>
</html>
```